ecommerce website design for pool store

I need a homepage designed for an e-commerce store for a pool shop. It will be similar to https://www.aquabrite.com.au/ but not an exact copy (ie. the icons, photos and colour scheme need to be different). aquabrite.com.au is one of our competitors but we love everything about their website.
I have attached the logo for this site. We want the background to be white and the colours used on the site to be the blue from the logo and the blue and green used on www.hopscotchyouth.com.au
I want the same layout for the logo, search and menu bar at the top along with the 'shop filter cartidges' feature button
Under that a similar slideshow
Under that, the categories with the logos, the best sellers, trending now (but call this 'latest products') and all the other same elements as on this example site.

```html
<!DOCTYPE html>
<html lang="en">
<head>
<meta charset="utf-8">
<title>Clearwater Pool Co – Home</title>
<link href="https://fonts.googleapis.com/css2?family=Bebas+Neue&family=Open+Sans:wght@400;600;700&display=swap" rel="stylesheet">
<style>
:root{
  --blue:#1f5fb8;
  --navy:#1c3f8e;
  --sky:#2f8fe0;
  --green:#a8c73b;
  --ink:#2b2b2b;
  --muted:#666;
  --line:#dcdcdc;
  --nav:#e8eef4;
  --grey:#f2f2f2;
  --dark:#222325;
  --white:#fff;
}
*{box-sizing:border-box;margin:0;padding:0}
html,body{width:1200px;height:4286px;overflow:hidden;background:var(--white)}
body{position:relative;font-family:"Open Sans",sans-serif;color:var(--ink)}
.abs{position:absolute}
.heading{font-family:"Bebas Neue",sans-serif;font-weight:400;color:var(--ink);letter-spacing:.5px}

.topbar{top:8px;left:0;width:1200px;font-size:14px;color:var(--ink)}
.topbar .perks{position:absolute;left:280px;top:0}
.topbar .account{position:absolute;left:915px;top:0}

.brand{left:111px;top:10px;width:140px;height:140px;border:3px solid var(--blue);border-radius:50%;display:flex;align-items:center;justify-content:center;text-align:center;font-weight:700;color:var(--blue);font-size:15px;line-height:1.2}
.search{left:306px;top:73px;width:536px;height:50px;border:1px solid #bbb;border-radius:4px;padding:0 16px;display:flex;align-items:center;justify-content:space-between;color:#777;font-size:15px}
.btn{background:var(--green);color:var(--white);font-weight:700;border-radius:26px;display:flex;align-items:center;justify-content:center;text-transform:uppercase}
.shop-filters{left:855px;top:71px;width:233px;height:54px;font-size:16px}

.nav{top:158px;left:0;width:1200px;height:48px;background:var(--nav)}
.nav ul{list-style:none;display:flex;justify-content:space-between;padding:0 100px 0 116px;height:48px;align-items:center;font-family:"Bebas Neue",sans-serif;font-size:22px;color:var(--ink)}

.hero{top:206px;left:0;width:1200px;height:554px;background:linear-gradient(120deg,#1e5bbf 0%,#2b7fd6 55%,#46a5ea 100%);overflow:hidden}
.hero-title{left:111px;top:112px;font-family:"Bebas Neue",sans-serif;font-size:72px;color:var(--white);line-height:1}
.hero-text{left:112px;top:210px;width:440px;font-size:22px;font-weight:600;color:var(--white);line-height:1.55}
.hero-cta{left:111px;top:313px;width:170px;height:58px;font-size:18px}
.hero-product{left:545px;top:30px;width:640px;height:420px;border-radius:48% 52% 40% 45%;background:radial-gradient(circle at 55% 45%,#2c8ef2 0%,#1f6fd6 35%,rgba(30,40,60,.55) 70%,rgba(30,80,170,0) 72%)}
.arrow{width:26px;height:26px}

.section-title{width:1200px;left:0;text-align:center;font-size:44px}
.cat{display:flex;align-items:center}
.cat-icon{width:92px;height:92px;border:2px solid #d6d6d6;border-radius:50%;display:flex;align-items:center;justify-content:center;background:var(--white)}
.cat-icon span{width:46px;height:46px;border-radius:50%;background:linear-gradient(135deg,#dfeeb0,#b9d66a)}
.cat-label{margin-left:16px;font-size:20px;color:var(--ink)}

.band-grey{top:1389px;left:0;width:1200px;height:620px;background:var(--grey)}
.card{width:235px;height:388px;background:var(--white);border:1px solid var(--line);border-radius:4px;overflow:hidden}
.card-img{height:198px;margin:0}
.card-name{position:absolute;left:15px;top:224px;width:210px;font-size:17px;line-height:1.7}
.card-price{position:absolute;left:15px;top:286px;font-size:16px}
.card-btn{position:absolute;left:14px;top:324px;width:136px;height:44px;font-size:16px;font-weight:600}

.why{top:2652px;left:0;width:1200px;height:706px;background:linear-gradient(90deg,#7fb3dc 0%,#3f7dc8 45%,#1e4fa6 75%,#1a3f96 100%)}
.why-photo{left:0;top:0;width:620px;height:706px;background:linear-gradient(160deg,#cfd8df 0%,#9cc2e4 30%,#2f7ad0 60%,rgba(40,110,200,0) 100%)}
.why-title{left:651px;top:70px;font-family:"Bebas Neue",sans-serif;font-size:44px;color:var(--white)}
.why-item{left:651px;width:520px;display:flex}
.why-icon{width:106px;height:106px;border-radius:50%;background:rgba(255,255,255,.22);display:flex;align-items:center;justify-content:center;flex:none}
.why-copy{margin-left:20px;padding-top:8px;color:var(--white)}
.why-copy h3{font-size:22px;font-weight:600;margin-bottom:8px}
.why-copy p{font-size:16px;line-height:1.6;color:#dfe8f5;width:310px}

.brand-box{top:3523px;width:183px;height:102px;border:1px solid #cfcfcf;display:flex;align-items:center;justify-content:center;font-size:19px;font-weight:600;color:#555}

.footer{top:3702px;left:0;width:1200px;height:584px;background:var(--dark);color:#ddd}
.footer-curve{left:0;top:3680px;width:1200px;height:160px}
.footer-brand{left:113px;top:115px;width:216px;height:216px;border:4px solid var(--blue);border-radius:50%;display:flex;align-items:center;justify-content:center;text-align:center;color:var(--blue);font-weight:700;font-size:22px;line-height:1.25}
.f-col h4{font-family:"Bebas Neue",sans-serif;font-weight:400;font-size:19px;color:var(--white);margin-bottom:14px}
.f-col ul{list-style:none;font-size:16px;line-height:30.8px;color:#ddd}
.f-contact{left:112px;font-size:16px;color:#ddd;display:flex;gap:10px;align-items:flex-start}
.f-input{left:864px;top:173px;width:224px;height:42px;background:var(--white);border-radius:3px;color:#666;font-size:15px;padding:10px 14px}
.f-signup{left:864px;top:242px;width:88px;height:38px;font-size:15px;font-weight:600}
.pay{width:58px;height:37px;background:var(--white);border-radius:3px;font-size:11px;font-weight:600;color:#333;display:flex;align-items:center;justify-content:center}
.f-rule{left:110px;top:488px;width:978px;height:1px;background:#555}
.copyright{left:110px;top:520px;font-size:16px;color:#ddd}
.social{top:514px;height:34px;padding:0 10px;border:1.5px solid #ddd;border-radius:17px;font-size:11px;color:#ddd;display:flex;align-items:center}
</style>
</head>
<body>

<div class="abs topbar">
  <div class="perks">Free Shipping &nbsp;|&nbsp; Buy Now, Pay Later, Laterly &nbsp;|&nbsp; 60 Day Easy Returns</div>
  <div class="account">Login/Join &nbsp;&nbsp; Cart (0)</div>
</div>

<div class="abs brand">Clearwater<br>Pool Co</div>
<div class="abs search"><span>Search</span>
  <svg width="18" height="18" viewBox="0 0 18 18"><circle cx="7.5" cy="7.5" r="5.5" fill="none" stroke="#333" stroke-width="2"/><line x1="11.5" y1="11.5" x2="16" y2="16" stroke="#333" stroke-width="2.4" stroke-linecap="round"/></svg>
</div>
<div class="abs btn shop-filters">Shop Filter Cartidges</div>

<nav class="abs nav">
  <ul><li>Pumps</li><li>Filters</li><li>Chlorinators</li><li>Cleaners</li><li>Lights</li><li>Maintenance</li><li>Covers</li><li>Heaters</li><li>Spas</li><li>Chemicals</li></ul>
</nav>

<section class="abs hero">
  <div class="abs hero-product" role="img" aria-label="Blue pool pump with black motor"></div>
  <h1 class="abs hero-title">Pool Pumps</h1>
  <p class="abs hero-text">Duis aute irure dolor in reprehenderit in voluptate velit esse cilldolore.</p>
  <div class="abs btn hero-cta">Shop Now!</div>
  <svg class="abs arrow" style="left:44px;top:244px" viewBox="0 0 26 26"><polyline points="17,3 7,13 17,23" fill="none" stroke="#fff" stroke-width="3"/></svg>
  <svg class="abs arrow" style="left:1137px;top:244px" viewBox="0 0 26 26"><polyline points="9,3 19,13 9,23" fill="none" stroke="#fff" stroke-width="3"/></svg>
  <svg class="abs" style="left:0;top:0" width="1200" height="554" viewBox="0 0 1200 554">
    <path d="M0 425 Q560 650 1200 420 L1200 554 L0 554 Z" fill="#fff"/>
    <path d="M0 425 Q560 650 1200 420" fill="none" stroke="#1c3f8e" stroke-width="6"/>
    <path d="M0 437 Q560 662 1200 432" fill="none" stroke="#2f8fe0" stroke-width="4"/>
  </svg>
</section>

<h2 class="abs heading section-title" style="top:820px">Categories</h2>
<div class="abs cat" style="left:110px;top:912px"><div class="cat-icon" role="img" aria-label="Filter cartridges icon"><span></span></div><span class="cat-label">Filter Cartridges</span></div>
<div class="abs cat" style="left:435px;top:912px"><div class="cat-icon" role="img" aria-label="Pool cleaner icon"><span></span></div><span class="cat-label">Pool Cleaners</span></div>
<div class="abs cat" style="left:778px;top:912px"><div class="cat-icon" role="img" aria-label="Cleaner hose icon"><span></span></div><span class="cat-label">Pool Cleaner Spare Parts</span></div>
<div class="abs cat" style="left:110px;top:1017px"><div class="cat-icon" role="img" aria-label="Pool hose icon"><span></span></div><span class="cat-label">Pool Hoses</span></div>
<div class="abs cat" style="left:435px;top:1017px"><div class="cat-icon" role="img" aria-label="Spa parts icon"><span></span></div><span class="cat-label">Spa Parts</span></div>
<div class="abs cat" style="left:778px;top:1017px"><div class="cat-icon" role="img" aria-label="Pool pump icon"><span></span></div><span class="cat-label">Pool Pumps</span></div>
<div class="abs cat" style="left:110px;top:1119px"><div class="cat-icon" role="img" aria-label="Pool cover icon"><span></span></div><span class="cat-label">Pool Covers</span></div>
<div class="abs cat" style="left:435px;top:1119px"><div class="cat-icon" role="img" aria-label="Cleaning net icon"><span></span></div><span class="cat-label">Cleaning Equipment</span></div>
<div class="abs cat" style="left:778px;top:1119px"><div class="cat-icon" role="img" aria-label="Chlorine drop icon"><span></span></div><span class="cat-label">Pool Chlorinators</span></div>
<div class="abs cat" style="left:110px;top:1224px"><div class="cat-icon" role="img" aria-label="Pool heater icon"><span></span></div><span class="cat-label">Pool Heaters</span></div>
<div class="abs cat" style="left:435px;top:1224px"><div class="cat-icon" role="img" aria-label="Chemical bottle icon"><span></span></div><span class="cat-label">Pool &amp; Spa Chemicals</span></div>
<div class="abs cat" style="left:778px;top:1224px"><div class="cat-icon" role="img" aria-label="Skimmer fitting icon"><span></span></div><span class="cat-label">Skimmers &amp; Fittings</span></div>

<div class="abs band-grey"></div>
<h2 class="abs heading section-title" style="top:1445px">Best Sellers</h2>
<svg class="abs arrow" style="left:44px;top:1723px" viewBox="0 0 26 26"><polyline points="17,3 7,13 17,23" fill="none" stroke="#777" stroke-width="2.5"/></svg>
<svg class="abs arrow" style="left:1137px;top:1723px" viewBox="0 0 26 26"><polyline points="9,3 19,13 9,23" fill="none" stroke="#777" stroke-width="2.5"/></svg>

<div class="abs card" style="left:110px;top:1541px"><div class="card-img" role="img" aria-label="Filter cartridge with blue end cap" style="background:radial-gradient(circle at 60% 50%,#1f4fb0 0 22%,#eef2f7 23% 60%,#fff 61%)"></div><p class="card-name">Lorem ipsu olor sitame conse ctetur ad</p><p class="card-price">$567.98</p><div class="btn card-btn">Add to cart</div></div>
<div class="abs card" style="left:358px;top:1541px"><div class="card-img" role="img" aria-label="Sand filter tank with valve" style="background:radial-gradient(ellipse at 55% 45%,#f1f0e6 0 28%,#444 30% 34%,#fff 46%)"></div><p class="card-name">Lorem ipsu olor sitame conse ctetur ad</p><p class="card-price">$567.98</p><div class="btn card-btn">Add to cart</div></div>
<div class="abs card" style="left:606px;top:1541px"><div class="card-img" role="img" aria-label="Pool maintenance kit in blue tub" style="background:linear-gradient(150deg,#e6f2fb 0%,#3b8de0 50%,#dbeaf6 100%)"></div><p class="card-name">Lorem ipsu olor sitame conse ctetur ad</p><p class="card-price">$567.98</p><div class="btn card-btn">Add to cart</div></div>
<div class="abs card" style="left:854px;top:1541px"><div class="card-img" role="img" aria-label="Pool cleaner parts in a case" style="background:linear-gradient(160deg,#9aa6a0 0%,#5d6a66 50%,#c9d0cc 100%)"></div><p class="card-name">Lorem ipsu olor sitame conse ctetur ad</p><p class="card-price">$567.98</p><div class="btn card-btn">Add to cart</div></div>

<h2 class="abs heading section-title" style="top:2079px">Latest Products</h2>
<svg class="abs arrow" style="left:44px;top:2355px" viewBox="0 0 26 26"><polyline points="17,3 7,13 17,23" fill="none" stroke="#777" stroke-width="2.5"/></svg>
<svg class="abs arrow" style="left:1137px;top:2355px" viewBox="0 0 26 26"><polyline points="9,3 19,13 9,23" fill="none" stroke="#777" stroke-width="2.5"/></svg>

<div class="abs card" style="left:110px;top:2173px"><div class="card-img" role="img" aria-label="White pleated filter element" style="background:radial-gradient(ellipse at 50% 50%,#d9d9d9 0 40%,#fff 42%)"></div><p class="card-name">Lorem ipsu olor sitame conse ctetur ad</p><p class="card-price">$567.98</p><div class="btn card-btn">Add to cart</div></div>
<div class="abs card" style="left:358px;top:2173px"><div class="card-img" role="img" aria-label="Pool light with coiled cable" style="background:radial-gradient(ellipse at 50% 55%,#777 0 20%,#bbb 40%,#fff 62%)"></div><p class="card-name">Lorem ipsu olor sitame conse ctetur ad</p><p class="card-price">$567.98</p><div class="btn card-btn">Add to cart</div></div>
<div class="abs card" style="left:606px;top:2173px"><div class="card-img" role="img" aria-label="Carbon mesh filter cartridge" style="background:linear-gradient(150deg,#fff 15%,#333 35%,#555 65%,#fff 85%)"></div><p class="card-name">Lorem ipsu olor sitame conse ctetur ad</p><p class="card-price">$567.98</p><div class="btn card-btn">Add to cart</div></div>
<div class="abs card" style="left:854px;top:2173px"><div class="card-img" role="img" aria-label="Compact blue pool pump" style="background:radial-gradient(ellipse at 55% 50%,#2f87e8 0 25%,#2a2a2a 30% 34%,#fff 48%)"></div><p class="card-name">Lorem ipsu olor sitame conse ctetur ad</p><p class="card-price">$567.98</p><div class="btn card-btn">Add to cart</div></div>

<section class="abs why">
  <div class="abs why-photo" role="img" aria-label="Hand lifting a yellow and blue robotic pool cleaner from the water"></div>
  <h2 class="abs why-title">Why Choose Us</h2>
  <div class="abs why-item" style="top:157px">
    <div class="why-icon"><svg width="46" height="34" viewBox="0 0 46 34"><rect x="2" y="4" width="26" height="20" fill="#fff"/><path d="M28 10h9l7 8v6H28z" fill="#fff"/><circle cx="11" cy="27" r="5" fill="#fff" stroke="#4c7fc6" stroke-width="2"/><circle cx="35" cy="27" r="5" fill="#fff" stroke="#4c7fc6" stroke-width="2"/></svg></div>
    <div class="why-copy"><h3>Free Shipping</h3><p>Duis aute irure dolor in reprehenderit in voluptate velit esse cillu.</p></div>
  </div>
  <div class="abs why-item" style="top:287px">
    <div class="why-icon"><svg width="40" height="36" viewBox="0 0 40 36"><path d="M5 24V19a15 15 0 0 1 30 0v5" fill="none" stroke="#fff" stroke-width="4"/><rect x="2" y="20" width="9" height="14" rx="3" fill="#fff"/><rect x="29" y="20" width="9" height="14" rx="3" fill="#fff"/></svg></div>
    <div class="why-copy"><h3>Lifetime After-sales Support</h3><p>Duis aute irure dolor in reprehenderit in voluptate velit esse cillu.</p></div>
  </div>
  <div class="abs why-item" style="top:417px">
    <div class="why-icon"><svg width="40" height="36" viewBox="0 0 40 36"><path d="M16 4 2 16l14 12v-7c10 0 17 3 22 11-1-12-8-20-22-21z" fill="#fff"/></svg></div>
    <div class="why-copy"><h3>60 Day Returns</h3><p>Duis aute irure dolor in reprehenderit in voluptate velit esse cillu.</p></div>
  </div>
  <div class="abs why-item" style="top:550px">
    <div class="why-icon"><svg width="38" height="38" viewBox="0 0 38 38"><rect x="2" y="16" width="8" height="20" fill="#fff"/><path d="M13 16 21 3c3 0 5 2 4 6l-2 6h10c3 0 4 3 3 5l-4 13c-1 2-2 3-4 3H13z" fill="#fff"/></svg></div>
    <div class="why-copy"><h3>Game-changing Value</h3><p>Duis aute irure dolor in reprehenderit in voluptate velit esse cillu.</p></div>
  </div>
</section>

<h2 class="abs heading section-title" style="top:3434px">Brands We Love</h2>
<svg class="abs arrow" style="left:44px;top:3561px" viewBox="0 0 26 26"><polyline points="17,3 7,13 17,23" fill="none" stroke="#777" stroke-width="2.5"/></svg>
<svg class="abs arrow" style="left:1137px;top:3561px" viewBox="0 0 26 26"><polyline points="9,3 19,13 9,23" fill="none" stroke="#777" stroke-width="2.5"/></svg>
<div class="abs brand-box" style="left:110px">Tidewell</div>
<div class="abs brand-box" style="left:308px">Bluecrest</div>
<div class="abs brand-box" style="left:508px">Aquaform</div>
<div class="abs brand-box" style="left:706px">Reefline</div>
<div class="abs brand-box" style="left:905px">Saltmere</div>

<footer class="abs footer">
  <div class="abs footer-brand">Clearwater<br>Pool Co</div>

  <div class="abs f-col" style="left:419px;top:125px"><h4>Quick Links</h4><ul><li>Pumps</li><li>Filters</li><li>Chlorinators</li><li>Cleaners</li><li>Lights</li><li>Covers</li><li>Heaters</li><li>Hoses</li></ul></div>
  <div class="abs f-col" style="left:556px;top:125px"><h4>Support</h4><ul><li>Shipping</li><li>Returns</li><li>Payment</li><li>Laterly</li><li>Swiftly</li><li>Splitsy</li><li>Track Your Order</li><li>Contact Us</li></ul></div>
  <div class="abs f-col" style="left:727px;top:125px"><h4>Info</h4><ul><li>About us</li><li>Reviews</li><li>Blog</li><li>Free Quote</li><li>Login</li><li>Register</li></ul></div>
  <div class="abs f-col" style="left:864px;top:125px"><h4>Newsletter Sign Up</h4></div>
  <div class="abs f-input">Email Address</div>
  <div class="abs btn f-signup">Sign Up</div>

  <div class="abs pay" style="left:871px;top:316px">Centra</div>
  <div class="abs pay" style="left:944px;top:316px">Tapwise</div>
  <div class="abs pay" style="left:1016px;top:316px">Walleto</div>
  <div class="abs pay" style="left:871px;top:370px">Orbix</div>
  <div class="abs pay" style="left:944px;top:370px">Cartly</div>
  <div class="abs pay" style="left:1016px;top:370px">Norda</div>

  <div class="abs f-contact" style="top:350px"><svg width="14" height="16" viewBox="0 0 14 16"><path d="M3 1l3 3-2 2c1 2 3 4 5 5l2-2 3 3-2 3C6 14 0 8 1 3z" fill="#ddd"/></svg>1 800 555 0142</div>
  <div class="abs f-contact" style="top:388px"><svg width="16" height="14" viewBox="0 0 16 14"><rect x="1" y="2" width="14" height="10" fill="#ddd"/><polyline points="1,2 8,8 15,2" fill="none" stroke="#222325" stroke-width="1.5"/></svg>hello@clearwaterpoolco.com</div>
  <div class="abs f-contact" style="top:426px;line-height:1.2"><svg width="12" height="16" viewBox="0 0 12 16"><path d="M6 0a6 6 0 0 1 6 6c0 4-6 10-6 10S0 10 0 6a6 6 0 0 1 6-6z" fill="#ddd"/><circle cx="6" cy="6" r="2" fill="#222325"/></svg><span>14 Harbour Lane Gosford,<br>NSW 2250</span></div>

  <div class="abs f-rule"></div>
  <p class="abs copyright">© 2022, Clearwater Pool Co. All rights reserved.</p>
  <div class="abs social" style="left:842px">Splashbook</div>
  <div class="abs social" style="left:936px">Linkpool</div>
  <div class="abs social" style="left:1018px">Chirply</div>
</footer>

<svg class="abs footer-curve" viewBox="0 0 1200 160" aria-hidden="true">
  <path d="M0 0 H1200 V40 Q560 -40 0 150 Z" fill="#fff"/>
  <path d="M0 150 Q560 -40 1200 40" fill="none" stroke="#1c3f8e" stroke-width="6"/>
  <path d="M0 140 Q560 -50 1200 30" fill="none" stroke="#2f8fe0" stroke-width="4"/>
</svg>

</body>
</html>
```